Präsentationsvorlagen für Portal für Auftragsvermittlungen in der Immobilienbranche
Zielgruppe
Portal für Auftragsvermittlungen in der Immobilienbranche
Bei uns können Immobilienunternehmen kurzfristig Personal für einzelne Arbeitseinsätze über unser Portal buchen.
Aufgabenstellung
Ruhiges Design, Farbpalette im Logo benutzen, darf Bilder enthalten ist aber nicht zwingend
Schriftart Gotham oder Montserrat
Wie benötigen somit eine Präsentationsvorlage zur Vorstellung unseres Unternehmens

```html
<!DOCTYPE html>
<html lang="de">
<head>
<meta charset="utf-8">
<title>Domivo – Präsentationsvorlage</title>
<link rel="stylesheet" href="https://fonts.googleapis.com/css2?family=Montserrat:wght@400;500;700&display=swap">
<style>
:root{
  --navy:#2a3f78;
  --ink:#111318;
  --text:#222;
  --rule:#3b4f86;
  --faint:#eef2f9;
  --faint-2:#f6f8fc;
  --page:#ffffff;
}
*{box-sizing:border-box;margin:0;padding:0}
html,body{width:1200px;height:2738px;overflow:hidden;background:var(--page)}
body{position:relative;font-family:"Montserrat",sans-serif;color:var(--text)}
.slide{position:absolute;left:184px;width:766px;height:430px;background:#fff;
  box-shadow:6px 8px 10px rgba(0,0,0,.22);border-bottom:4px solid var(--navy);overflow:hidden}
.slide-bg{position:absolute;inset:0;background:linear-gradient(180deg,var(--faint-2) 0%,var(--faint) 100%)}
.slide-head{position:absolute;left:0;top:0;width:100%;height:118px;background:linear-gradient(90deg,rgba(255,255,255,.7),rgba(255,255,255,.95));border-bottom:1.5px solid var(--rule)}
.slide-title{position:absolute;left:59px;top:72px;font-size:22px;font-weight:700;color:var(--ink)}
.brand-name{position:absolute;right:34px;top:72px;font-size:22px;font-weight:500;color:var(--navy);line-height:1.2}
.slide-body{position:absolute;left:59px;top:140px;font-size:15.5px;line-height:19px;color:var(--ink)}

/* title slide */
.hero{position:absolute;left:0;top:0;width:100%;height:385px;
  background:radial-gradient(circle at 82% 25%,#e8a070 0,#3d6a9a 12%,transparent 30%),
  radial-gradient(circle at 45% 75%,#c88a5a 0,#2d5d8e 18%,transparent 40%),
  linear-gradient(135deg,#1a2a44 0%,#20406a 55%,#162236 100%)}
.hero-title{position:absolute;left:59px;top:26px;font-size:44px;font-weight:700;color:#fff}
.hero-sub{position:absolute;left:66px;top:87px;font-size:18.5px;line-height:22px;color:#fff}
.hero-sub p+p{margin-top:10px}
.hero-foot{position:absolute;left:0;top:385px;width:100%;height:41px;display:flex;justify-content:center;align-items:center}
.hero-foot .brand-name{position:static;font-size:14px}

/* goal */
.illustration{position:absolute;left:396px;top:155px;width:340px;height:225px;border-radius:8px;
  background:linear-gradient(180deg,#eef3fb 0%,#c9d8ef 70%,#e9eef7 100%)}

/* benefits */
.benefit{position:absolute;display:flex;gap:16px;font-size:15.5px;line-height:19px;color:var(--ink)}
.benefit svg{flex:none}

/* quote */
.quote-box{position:absolute;left:494px;top:0;width:272px;height:160px;border-left:1px solid #dde3ee;border-bottom:1px solid #dde3ee}
.quote{position:absolute;left:130px;top:216px;font-size:19.5px;line-height:29px;color:var(--text)}
.chevrons{position:absolute;left:10px;top:192px}

/* contact */
.contact-lead{font-weight:700;font-size:15.5px}
.contact{margin-top:27px;font-size:15.5px;line-height:25px}
.contact strong{font-weight:700}
</style>
</head>
<body>

<section class="slide" style="top:178px">
  <div class="hero" role="img" aria-label="Foto: Geschäftsmann tippt auf leuchtende Finanzdiagramme über einem Tablet"></div>
  <h1 class="hero-title">Willkommen!</h1>
  <div class="hero-sub">
    <p>zum <strong>Immobilienportal</strong></p>
    <p>welches Unternehmen und<br>Immobilienprofis verbindet</p>
  </div>
  <div class="hero-foot"><span class="brand-name">Domivo</span></div>
</section>

<section class="slide" style="top:660px">
  <div class="slide-bg" role="img" aria-label="Dezente Hausfassaden als Hintergrund"></div>
  <div class="slide-head"></div>
  <h2 class="slide-title">Unser Ziel</h2>
  <span class="brand-name">Domivo</span>
  <div class="slide-body" style="top:142px">
    <p>Die Immobilienbranche benötigt eine<br>Effizienzsteigerung und eine<br>flexiblere Performance. Wir bieten<br>Ihnen die Möglichkeit, schnell<br>zusätzliche Ressourcen zu buchen<br>um Ihre Leistungen an Ihre<br>kurzfristigen Bedürfnisse anzupassen.</p>
    <p style="margin-top:19px">Ferienvertretungen,<br>Krankheitsausfälle, allfällige<br>Personallücken oder -engpässe, wir<br>sind für Sie da.</p>
  </div>
  <div class="illustration" role="img" aria-label="Illustration: Menschen vor Häusern und Hochhäusern mit steigender Umsatzkurve"></div>
</section>

<section class="slide" style="top:1143px">
  <div class="slide-bg" role="img" aria-label="Dezente Hausfassaden als Hintergrund"></div>
  <div class="slide-head"></div>
  <h2 class="slide-title">Was bringt mir Domivo?</h2>
  <span class="brand-name">Domivo</span>
  <div class="benefit" style="left:66px;top:157px">
    <svg width="32" height="40" viewBox="0 0 32 40" fill="none" stroke="#111" stroke-width="1.6"><path d="M2 2h20l8 8v28H2z"/><path d="M22 2v8h8"/><path d="M10 22l4 4 8-8"/></svg>
    <span>Einfache Auftragsausschreibung/-<br>abwicklung</span>
  </div>
  <div class="benefit" style="left:414px;top:157px">
    <svg width="32" height="40" viewBox="0 0 32 40" fill="none" stroke="#111" stroke-width="1.6"><path d="M2 2h20l8 8v28H2z"/><path d="M22 2v8h8"/><circle cx="16" cy="17" r="3.5"/><path d="M9 27c1-4 4-5 7-5s6 1 7 5M8 31h16M8 34h16"/></svg>
    <span>Einfache Abrechnung, keine<br>Lohnadministration</span>
  </div>
  <div class="benefit" style="left:66px;top:257px">
    <svg width="40" height="40" viewBox="0 0 40 40" fill="none" stroke="#111" stroke-width="1.6"><path d="M2 2h20l8 8v28H2z"/><path d="M22 2v8h8"/><path d="M7 16h16M7 21h16M7 26h11M7 31h8"/><path d="M20 34l16-16 3 3-16 16h-3z"/></svg>
    <span>Zutreffende Agents werden<br>vorgeschlagen</span>
  </div>
  <div class="benefit" style="left:414px;top:257px">
    <svg width="32" height="40" viewBox="0 0 32 40" fill="none" stroke="#111" stroke-width="1.6"><path d="M2 2h20l8 8v28H2z"/><path d="M22 2v8h8"/><path d="M7 18v15h18"/><path d="M9 30l4-8 4 6 6-10"/></svg>
    <span>Übersicht der Aufträge</span>
  </div>
</section>

<section class="slide" style="top:1636px">
  <div class="slide-bg" style="background:linear-gradient(200deg,#fff 40%,#e8edf7 100%)"></div>
  <div class="slide-head" style="background:transparent"></div>
  <div class="quote-box"></div>
  <h2 class="slide-title" style="font-size:20px;top:76px">Dies ist eine Vorlage</h2>
  <span class="brand-name">Domivo</span>
  <svg class="chevrons" width="92" height="92" viewBox="0 0 92 92" fill="none" stroke="#dfe5f2" stroke-width="14"><path d="M8 8l38 38-38 38M46 8l38 38-38 38"/></svg>
  <p class="quote">„Hier könnte ein Zitat oder ähnliches stehen,<br>Um die Firma zu bewerben.“</p>
</section>

<section class="slide" style="top:2123px">
  <div class="slide-bg" role="img" aria-label="Dezente Hausfassaden als Hintergrund"></div>
  <div class="slide-head"></div>
  <h2 class="slide-title">Vielen Dank</h2>
  <span class="brand-name">Domivo</span>
  <div class="slide-body" style="top:143px">
    <p class="contact-lead">Bei Fragen stehen wir dir gerne zur Verfügung.</p>
    <p class="contact"><strong>Domivo AG</strong><br>Lindenweg 12<br>8001 Musterdorf<br>T +41 79 000 12 34<br>info@domivo.ch<br>www.domivo.ch</p>
  </div>
</section>

</body>
</html>
```